Design professional, clean and neat beauty clinic

design an instagram style flyer similar style but have my own branding. Like they have their own. Must look different but also similar/better in professionalism. source file also needed.

Font styles to use
Sans Serif

```html
<!DOCTYPE html>
<html lang="en">
<head>
<meta charset="utf-8">
<title>Lift &amp; Restore Package</title>
<link href="https://fonts.googleapis.com/css2?family=Montserrat:wght@400;500;600;700;800&display=swap" rel="stylesheet">
<style>
  :root {
    --sky: #19c3ee;
    --sunshine: #ffcc0d;
    --sunshine-deep: #e6b400;
    --ink: #333333;
    --text-dark: #222222;
    --white: #ffffff;
    --skin-light: #f3dccd;
    --skin-mid: #e8c4ae;
  }
  * { box-sizing: border-box; margin: 0; padding: 0; }
  html, body {
    width: 1200px;
    height: 1200px;
    overflow: hidden;
    background: var(--sky);
  }
  .flyer {
    position: relative;
    width: 1200px;
    height: 1200px;
    background: var(--sky);
    font-family: "Montserrat", sans-serif;
    overflow: hidden;
  }
  .model-photo {
    position: absolute;
    left: 600px;
    top: 0;
    width: 600px;
    height: 980px;
    background:
      radial-gradient(ellipse 46% 50% at 55% 42%, var(--skin-light) 0%, var(--skin-mid) 55%, rgba(25,195,238,0) 100%),
      radial-gradient(ellipse 30% 40% at 90% 35%, rgba(255,255,255,0.55) 0%, rgba(25,195,238,0) 100%);
  }
  .sun-band {
    position: absolute;
    left: 0;
    top: 0;
    width: 1200px;
    height: 1200px;
  }
  .package-tag {
    position: absolute;
    left: 53px;
    top: 167px;
    width: 384px;
    height: 79px;
    background: var(--sunshine);
    color: var(--white);
    font-weight: 500;
    font-size: 51px;
    letter-spacing: 1px;
    line-height: 79px;
    text-align: center;
  }
  .title {
    position: absolute;
    left: 52px;
    top: 272px;
    color: var(--white);
    font-weight: 800;
    font-size: 84px;
    line-height: 89px;
    letter-spacing: 1px;
    text-transform: uppercase;
  }
  .description {
    position: absolute;
    left: 54px;
    top: 484px;
    width: 560px;
    color: var(--white);
    font-weight: 400;
    font-size: 33px;
    line-height: 44.5px;
  }
  .description p + p { margin-top: 44px; }
  .price-pill {
    position: absolute;
    left: 656px;
    top: 1008px;
    width: 419px;
    height: 89px;
    border-radius: 45px;
    background: var(--ink);
    color: var(--white);
    font-weight: 700;
    font-size: 42px;
    line-height: 89px;
    text-align: center;
    letter-spacing: 0.5px;
  }
  .call-line {
    position: absolute;
    left: 600px;
    top: 1112px;
    width: 530px;
    color: var(--text-dark);
    font-weight: 400;
    font-size: 34px;
    text-align: center;
  }
</style>
</head>
<body>
  <main class="flyer">
    <div class="model-photo" role="img" aria-label="Portrait of a woman with eyes closed and water splashing across her face, against a sky-blue background"></div>

    <svg class="sun-band" viewBox="0 0 1200 1200" aria-hidden="true">
      <polygon points="0,1122 1200,839 1200,1200 0,1200" fill="var(--sunshine)"/>
      <polygon points="0,1094 700,938 0,1122" fill="var(--sunshine-deep)"/>
    </svg>

    <div class="package-tag">PACKAGE</div>

    <h1 class="title">Lift &amp;<br>Restore</h1>

    <div class="description">
      <p>The lift and restore package consist of 4ml premium product which can be used in the mid and lower face to restore volume loss.</p>
      <p>Restoring that volume loss will help you reverse the signs of aging.</p>
    </div>

    <div class="price-pill">FOR £475 ONLY</div>
    <div class="call-line">Call today 0161 555 0192</div>
  </main>
</body>
</html>
```